Power Point Template for Company

I would like a power point template for my company. This will be the template that we use for all presentations. I have attached our company logo and would like it incorporated into the template. Thanks.

```html
<!DOCTYPE html>
<html lang="en">
<head>
<meta charset="utf-8">
<title>Vantora Presentation Template</title>
<link href="https://fonts.googleapis.com/css2?family=Montserrat:wght@400;500;600;700;800&display=swap" rel="stylesheet">
<style>
:root{
  --orange:#ff7a00;
  --ink:#231f20;
  --grey:#8a8a8a;
  --light:#d9d9d9;
  --paper:#ffffff;
  --stage:#e6e6e6;
}
*{box-sizing:border-box;margin:0;padding:0}
html,body{width:1042px;height:1200px;overflow:hidden;background:var(--stage)}
body{font-family:"Montserrat",Arial,sans-serif;color:var(--ink)}
.canvas{position:relative;width:1042px;height:1200px;overflow:hidden;background:var(--stage)}
.slide{position:absolute;width:543px;height:306px;background:var(--paper);transform:scale(.5815);transform-origin:0 0;overflow:hidden;box-shadow:0 3px 8px rgba(0,0,0,.22)}
.slide > *{position:absolute}
.c1{left:36px}.c2{left:363px}.c3{left:691px}
.r1{top:40px}.r2{top:227px}.r3{top:418px}.r4{top:605px}.r5{top:794px}.r6{top:983px}
.orange{background:var(--orange)}
.dark{background:var(--ink)}
.photo{background:linear-gradient(150deg,#b9c2c9 0%,#8d969d 45%,#5a5f63 100%)}
.photo.warm{background:linear-gradient(160deg,#cfc6bb 0%,#9a8f84 50%,#4d4a47 100%)}
.title{font-weight:700;font-size:17px;line-height:1.2}
.uline{width:38px;height:3px;background:var(--orange)}
.p{font-size:6px;line-height:1.45;color:var(--grey)}
.p.w{color:#fff}
.h{font-weight:700;font-size:10px}
.foot{left:22px;top:272px;width:510px;height:20px}
.mark{position:absolute;left:0;top:0;font-weight:800;font-size:11px;letter-spacing:.5px;color:var(--ink)}
.rule{position:absolute;left:0;right:8px;top:15px;height:1px;background:var(--orange)}
.pg{position:absolute;right:0;top:12px;width:7px;height:7px;background:var(--orange)}
.sq{width:20px;height:20px}
.num{font-weight:700;color:var(--orange)}
.list-item .h{font-size:10.5px}
.list-item .p{margin-top:3px;width:200px}
svg text{font-family:"Montserrat",Arial,sans-serif}
</style>
</head>
<body>
<div class="canvas">

<!-- 1 Cover -->
<section class="slide c1 r1">
  <div class="orange" style="left:29px;top:0;width:125px;height:10px"></div>
  <div style="left:36px;top:40px;font-weight:800;font-size:30px;letter-spacing:1px">VANTORA</div>
  <div style="left:30px;top:145px;width:3px;height:82px" class="orange"></div>
  <div style="left:40px;top:143px;font-size:13px">Presentation</div>
  <div style="left:40px;top:158px;font-size:31px;font-weight:800;color:var(--orange)">Business</div>
  <div style="left:40px;top:191px;font-size:26px;font-weight:700">Marketing</div>
  <div style="left:52px;top:272px;font-size:8px;letter-spacing:2.5px">www.website.com</div>
  <svg style="left:258px;top:55px" width="36" height="12"><g fill="var(--ink)"><circle cx="2" cy="2" r="1.3"/><circle cx="8" cy="2" r="1.3"/><circle cx="14" cy="2" r="1.3"/><circle cx="20" cy="2" r="1.3"/><circle cx="26" cy="2" r="1.3"/><circle cx="2" cy="8" r="1.3"/><circle cx="8" cy="8" r="1.3"/><circle cx="14" cy="8" r="1.3"/><circle cx="20" cy="8" r="1.3"/><circle cx="26" cy="8" r="1.3"/></g></svg>
  <div class="orange" style="left:341px;top:0;width:202px;height:20px"></div>
  <div class="orange" style="left:523px;top:0;width:20px;height:182px"></div>
  <div class="dark" style="left:215px;top:272px;width:328px;height:34px"></div>
  <div class="photo" role="img" aria-label="Two colleagues talking in a bright office" style="left:274px;top:31px;width:241px;height:246px"></div>
  <div class="dark" style="left:496px;top:37px;width:12px;height:12px"></div>
</section>

<!-- 2 Agenda -->
<section class="slide c2 r1">
  <div class="title" style="left:17px;top:14px">Text Added Here</div>
  <div class="uline" style="left:17px;top:42px"></div>
  <div class="photo warm" role="img" aria-label="Team meeting around a table seen from above" style="left:59px;top:72px;width:177px;height:182px"></div>
  <div class="list-item" style="left:266px;top:74px"><div class="h"><span class="num">1.</span> Lorem ipsum</div><div class="p">Lorem ipsum dolor sit amet, consectetuer adipiscing elit, sed diam nonummy nibh euismod tincid</div></div>
  <div class="list-item" style="left:266px;top:125px"><div class="h"><span class="num">2.</span> Lorem ipsum</div><div class="p">Lorem ipsum dolor sit amet, consectetuer adipiscing elit, sed diam nonummy nibh euismod tincid</div></div>
  <div class="list-item" style="left:266px;top:176px"><div class="h"><span class="num">3.</span> Lorem ipsum</div><div class="p">Lorem ipsum dolor sit amet, consectetuer adipiscing elit, sed diam nonummy nibh euismod tincid</div></div>
  <div class="list-item" style="left:266px;top:224px"><div class="h"><span class="num">4.</span> Lorem ipsum</div><div class="p">Lorem ipsum dolor sit amet, consectetuer adipiscing elit, sed diam nonummy nibh euismod tincid</div></div>
  <div class="foot"><span class="mark">VANTORA</span><i class="rule"></i><b class="pg"></b></div>
</section>

<!-- 3 Our Company -->
<section class="slide c3 r1">
  <div class="dark" style="left:27px;top:0;width:56px;height:27px"></div>
  <div class="dark" style="left:0;top:27px;width:27px;height:158px"></div>
  <div class="title" style="left:45px;top:33px;font-size:19px;line-height:1.25">Our<br>Company</div>
  <div class="uline" style="left:45px;top:90px"></div>
  <div class="p" style="left:45px;top:102px;width:192px;text-align:justify">Lorem ipsum dolor sit amet, consectetuer adipiscing elit, sed diam nonummy nibh euismod tincidunt ut laoreet dolore magna aliquam erat volutpat. Ut wisi enim ad minim veniam, quis nostrud exerci tation ullamcorper suscipit lobortis nisl ut aliquip ex ea commodo consequat. Duis autem vel eum iriure dolor in hendrerit in</div>
  <div class="p" style="left:45px;top:172px;width:192px;text-align:justify">Lorem ipsum dolor sit amet, consectetuer adipiscing elit, sed diam nonummy nibh euismod tincidunt ut laoreet dolore magna aliquam erat volutpat. Ut wisi enim ad minim veniam, quis nostrud exerci tation ullamcorper suscipit lobortis nisl ut aliquip ex ea commodo consequat. Duis autem vel eum iriure dolor in hendrerit in lorem ipsum dolor sit amet, consectetuer adipiscing elit, sed diam nonummy nibh euismod laoreet dolore magna aliquam erat volutpat.</div>
  <svg style="left:280px;top:50px" width="240" height="215">
    <g stroke="#fff" stroke-width="2" fill="none">
      <circle cx="49" cy="25" r="22" fill="var(--orange)" stroke="none"/><circle cx="49" cy="22" r="6"/><path d="M40 36c2-6 16-6 18 0"/>
      <circle cx="177" cy="25" r="22" fill="var(--ink)" stroke="none"/><circle cx="177" cy="25" r="9"/><path d="M168 25h18M177 16v18"/>
      <circle cx="49" cy="135" r="22" fill="var(--ink)" stroke="none"/><circle cx="49" cy="135" r="11"/><text x="49" y="139" fill="#fff" stroke="none" font-size="11" font-weight="700" text-anchor="middle">$</text>
      <circle cx="177" cy="135" r="22" fill="var(--orange)" stroke="none"/><circle cx="177" cy="135" r="10"/><path d="M172 135h10"/>
    </g>
    <g font-size="8.5" font-weight="700" text-anchor="middle" fill="var(--ink)">
      <text x="49" y="64">LOREM IPSUM</text><text x="177" y="64">LOREM IPSUM</text>
      <text x="49" y="174">LOREM IPSUM</text><text x="177" y="174">LOREM IPSUM</text>
    </g>
    <g font-size="5.5" text-anchor="middle" fill="var(--grey)">
      <text x="49" y="73">Lorem ipsum dolor sit amet,</text><text x="49" y="80">consectetuer adipiscing elit,</text><text x="49" y="87">sed diam nonummy nibh</text><text x="49" y="94">euismod tincid</text>
      <text x="177" y="73">Lorem ipsum dolor sit amet,</text><text x="177" y="80">consectetuer adipiscing elit,</text><text x="177" y="87">sed diam nonummy nibh</text><text x="177" y="94">euismod tincid</text>
      <text x="49" y="183">Lorem ipsum dolor sit amet,</text><text x="49" y="190">consectetuer adipiscing elit,</text><text x="49" y="197">sed diam nonummy nibh</text><text x="49" y="204">euismod tincid</text>
      <text x="177" y="183">Lorem ipsum dolor sit amet,</text><text x="177" y="190">consectetuer adipiscing elit,</text><text x="177" y="197">sed diam nonummy nibh</text><text x="177" y="204">euismod tincid</text>
    </g>
  </svg>
  <div class="foot"><span class="mark">VANTORA</span><i class="rule"></i><b class="pg"></b></div>
</section>

<!-- 4 About Us -->
<section class="slide c1 r2">
  <div class="title" style="left:26px;top:28px">About Us</div>
  <div class="uline" style="left:26px;top:58px"></div>
  <div class="p" style="left:26px;top:72px;width:280px">Lorem ipsum dolor sit amet, consectetuer adipiscing elit, sed diam nonummy nibh euismod tincidunt ut laoreet dolore magna aliquam erat volutpat. Ut wisi enim ad minim veniam, quis nostrud exerci tation ullamcorper suscipit lobortis nisl ut aliquip.</div>
  <div class="p" style="left:26px;top:108px;width:280px">Ex ea commodo consequat. Duis autem vel eum iriure dolor in hendrerit in vulputate velit esse molestie consequat, vel illum dolore eu feugiat nulla facilisis at vero eros et accumsan et iusto odio dignissim qui blandit praesent luptatum zzril delenit augue duis dolore te feugait nulla facilisi. Lorem ipsum dolor sit amet, cons ectetuer adipiscing elit, sed diam nonummy nibh euismod tincidunt ut laoreet dolore magna aliquam erat volutpat. Ut wisi enim ad minim veniam, quis nostrud exerci tation ullamcorper suscipit lobortis nisl ut aliquip ex ea commodo cons</div>
  <svg style="left:34px;top:193px" width="10" height="40"><path d="M1 1l6 4-6 4z" fill="var(--orange)"/><path d="M1 30l6 4-6 4z" fill="none" stroke="var(--orange)"/></svg>
  <svg style="left:164px;top:193px" width="10" height="40"><path d="M1 1l6 4-6 4z" fill="var(--orange)"/><path d="M1 30l6 4-6 4z" fill="none" stroke="var(--orange)"/></svg>
  <div class="p" style="left:46px;top:193px;width:110px">Lorem ipsum dolor sit amet, consectetuer adipiscing elit, sed diam nonummy nibh euismod</div>
  <div class="p" style="left:176px;top:193px;width:110px">Lorem ipsum dolor sit amet, consectetuer adipiscing elit, sed diam nonummy nibh euismod</div>
  <div class="p" style="left:46px;top:222px;width:110px">Lorem ipsum dolor sit amet, consectetuer adipiscing elit, sed diam nonummy nibh euismod</div>
  <div class="p" style="left:176px;top:222px;width:110px">Lorem ipsum dolor sit amet, consectetuer adipiscing elit, sed diam nonummy nibh euismod</div>
  <div class="dark" style="left:358px;top:159px;width:148px;height:95px"></div>
  <div class="orange" style="left:316px;top:214px;width:40px;height:40px"></div>
  <div class="photo" role="img" aria-label="Smiling man working on a laptop" style="left:334px;top:39px;width:155px;height:198px"></div>
  <div class="foot"><span class="mark">VANTORA</span><i class="rule"></i><b class="pg"></b></div>
</section>

<!-- 5 Values -->
<section class="slide c2 r2">
  <div class="orange sq" style="left:0;top:0"></div>
  <div style="left:37px;top:33px;font-size:23px;font-weight:700;line-height:34px">Lorem Ipsum<br>Dolor Sit<br>Ametkeeper.</div>
  <div class="dark" style="left:0;top:156px;width:218px;height:94px"></div>
  <div class="p w" style="left:37px;top:168px;width:160px;font-size:6.3px">Lorem ipsum dolor sit amet, consectetuer adipiscing elit, sed diam nonummy nibh euismod tincidunt erat volutpat.<br><br>Ut wisi enim ad minim veniam, quis nostrud exerci tation ullamcorper suscipit lobortis nisl ut aliquip ex ea commodo consequat.</div>
  <svg style="left:248px;top:47px" width="42" height="195">
    <rect width="42" height="42" fill="var(--orange)"/><g fill="#fff"><circle cx="21" cy="16" r="5"/><circle cx="12" cy="19" r="4"/><circle cx="30" cy="19" r="4"/><path d="M12 32c0-7 18-7 18 0zM5 32c0-5 9-6 10-4zM37 32c0-5-9-6-10-4z"/></g>
    <rect y="73" width="42" height="42" fill="var(--orange)"/><g fill="none" stroke="#fff" stroke-width="2"><circle cx="15" cy="83" r="3"/><circle cx="27" cy="83" r="3"/><path d="M11 107v-16h8v16M23 107v-16h8v16"/></g>
    <rect y="153" width="42" height="42" fill="var(--orange)"/><path d="M21 178c-8-6-10-10-7-13 2-2 5-1 7 2 2-3 5-4 7-2 3 3 1 7-7 13z" fill="#fff"/><path d="M8 184h10l10 3" stroke="#fff" stroke-width="2" fill="none"/>
  </svg>
  <div style="left:308px;top:50px"><div class="h" style="font-size:11px">We Before Me</div><div class="p" style="width:200px;margin-top:4px">ipsum dolor sit amet, cons ectetuer adipiscing elit, sed diam nonummy nibh euismod tincidunt ut laoreet</div></div>
  <div style="left:308px;top:122px"><div class="h" style="font-size:11px">We Are Good People</div><div class="p" style="width:215px;margin-top:4px">ipsum dolor sit amet, cons ectetuer adipiscing elit, sed diam nonummy nibh euismod tincidunt ut laoreet dolore magna aliquam erat volutpat.</div></div>
  <div style="left:308px;top:200px"><div class="h" style="font-size:11px">We Work with Heart</div><div class="p" style="width:200px;margin-top:4px">ipsum dolor sit amet, cons ectetuer adipiscing elit, sed diam nonummy nibh euismod tincidunt</div></div>
  <div class="foot"><span class="mark">VANTORA</span><i class="rule"></i><b class="pg"></b></div>
</section>

<!-- 6 Subject -->
<section class="slide c3 r2">
  <div class="orange" style="left:0;top:0;width:160px;height:20px"></div>
  <div class="title" style="left:30px;top:30px;font-size:23px;line-height:1.3">Subject<br>Title</div>
  <div class="uline" style="left:30px;top:103px"></div>
  <div class="p" style="left:30px;top:117px;width:118px;color:#555;font-size:6.4px">Lorem ipsum dolor sit amet, consectetuer adipiscing elit, sed diam nonummy nibh euismod tincidunt ut laoreet dolore magna aliquam erat volutpat. Ut wisi enim ad minim veniam, quis nostrud exerci tation ullamcorper suscipit lobortis nisl ut aliquip ex ea commodo consequat. Duis autem vel eum iriure.</div>
  <div class="photo" role="img" aria-label="Two colleagues reviewing work at a laptop" style="left:161px;top:0;width:101px;height:190px"></div>
  <div class="dark" style="left:227px;top:66px;width:316px;height:193px"></div>
  <div class="photo warm" role="img" aria-label="Business people shaking hands in an office" style="left:283px;top:104px;width:107px;height:175px"></div>
  <div style="left:402px;top:110px;font-size:14px;font-weight:700;color:var(--orange);line-height:1.15">Lorem Ipsum<br>Dolor Sit<br>Ametkeeper.</div>
  <div class="p w" style="left:405px;top:178px;width:120px;font-size:6.2px">Lorem ipsum dolor sit amet, consectetuer adipiscing<br><br>elit, sed diam nonummy nibh euismod tincidunt ut</div>
  <div class="foot"><span class="mark">VANTORA</span><i class="rule"></i><b class="pg"></b></div>
</section>

<!-- 7 Charts -->
<section class="slide c1 r3">
  <div class="dark" style="left:0;top:0;width:264px;height:150px"></div>
  <div style="left:24px;top:18px;color:#fff;font-size:15.5px;font-weight:700">Text Added Here</div>
  <div style="left:24px;top:43px;width:220px;color:#fff;font-size:8.2px;line-height:1.2">Lorem ipsum dolor sit amet, consectetuer adipiscing elit, sed diam nonummy nibh euismod tincidunt ut laoreet dolore magna aliquam erat volutpat. Ut wisi enim ad minim veniam<br><br>quis nostrud exerci tation ullamcorper suscipit lobortis nisl ut aliquip ex ea commodo conse-</div>
  <svg style="left:278px;top:32px" width="240" height="125" font-size="7">
    <g stroke="#ccc" stroke-width=".6"><path d="M22 5H238M22 21H238M22 37H238M22 52H238M22 68H238M22 84H238M22 100H238"/><path d="M22 5V100M238 5V100"/></g>
    <g fill="var(--ink)" text-anchor="end"><text x="17" y="8">60</text><text x="17" y="24">50</text><text x="17" y="40">40</text><text x="17" y="55">30</text><text x="17" y="71">20</text><text x="17" y="87">10</text><text x="17" y="103">0</text></g>
    <rect x="44" y="37" width="7" height="63" fill="var(--ink)"/><rect x="56" y="21" width="7" height="79" fill="var(--orange)"/>
    <rect x="92" y="83" width="7" height="17" fill="var(--orange)"/><rect x="104" y="45" width="7" height="55" fill="var(--ink)"/>
    <rect x="140" y="13" width="7" height="87" fill="var(--orange)"/><rect x="152" y="78" width="7" height="22" fill="var(--ink)"/>
    <rect x="186" y="18" width="7" height="82" fill="var(--ink)"/><rect x="198" y="52" width="7" height="48" fill="var(--orange)"/>
    <g text-anchor="middle" fill="var(--ink)"><text x="54" y="115">JAN</text><text x="102" y="115">FEB</text><text x="150" y="115">MAR</text><text x="196" y="115">APR</text></g>
  </svg>
  <svg style="left:18px;top:162px" width="244" height="100" font-size="5">
    <g stroke="#ccc" stroke-width=".5"><path d="M20 4H236M20 18H236M20 32H236M20 46H236M20 60H236M20 74H236M20 88H236"/></g>
    <g fill="var(--ink)" text-anchor="end"><text x="16" y="6">60</text><text x="16" y="20">50</text><text x="16" y="34">40</text><text x="16" y="48">30</text><text x="16" y="62">20</text><text x="16" y="76">10</text><text x="16" y="90">0</text></g>
    <polyline points="32,70 52,78 72,52 92,30 112,44 132,56 152,48 172,40 192,74" fill="none" stroke="var(--orange)" stroke-width="1.2"/>
    <polyline points="52,74 72,60 92,66 112,40 132,52 152,60 172,52 192,34" fill="none" stroke="var(--ink)" stroke-width="1.2"/>
    <g fill="var(--orange)"><circle cx="32" cy="70" r="1.8"/><circle cx="92" cy="30" r="1.8"/><circle cx="132" cy="56" r="1.8"/><circle cx="172" cy="40" r="1.8"/><circle cx="192" cy="74" r="1.8"/></g>
    <g fill="var(--ink)"><circle cx="52" cy="74" r="1.8"/><circle cx="92" cy="66" r="1.8"/><circle cx="112" cy="40" r="1.8"/><circle cx="152" cy="60" r="1.8"/><circle cx="192" cy="34" r="1.8"/></g>
    <g fill="var(--ink)" font-size="4" text-anchor="middle"><text x="32" y="97">TEXT 01</text><text x="52" y="97">TEXT 02</text><text x="72" y="97">TEXT 03</text><text x="92" y="97">TEXT 04</text><text x="112" y="97">TEXT 05</text><text x="132" y="97">TEXT 06</text><text x="152" y="97">TEXT 07</text><text x="172" y="97">TEXT 08</text><text x="192" y="97">TEXT 09</text></g>
  </svg>
  <svg style="left:272px;top:182px" width="12" height="50"><circle cx="6" cy="6" r="4" fill="var(--ink)"/><circle cx="6" cy="44" r="4" fill="var(--orange)"/></svg>
  <svg style="left:402px;top:182px" width="12" height="50"><circle cx="6" cy="6" r="4" fill="var(--orange)"/><circle cx="6" cy="44" r="4" fill="var(--ink)"/></svg>
  <div style="left:287px;top:182px"><div class="h" style="font-size:8px">Lorem ipsum</div><div class="p" style="width:105px;font-size:5px">Lorem ipsum dolor sit amet, consectetuer adipiscing elit, sed diam nonummy nibh euismod tincidunt ut laoreet</div></div>
  <div style="left:417px;top:182px"><div class="h" style="font-size:8px">Lorem ipsum</div><div class="p" style="width:105px;font-size:5px">Lorem ipsum dolor sit amet, consectetuer adipiscing elit, sed diam nonummy nibh euismod tincidunt ut laoreet</div></div>
  <div style="left:287px;top:220px"><div class="h" style="font-size:8px">Lorem ipsum</div><div class="p" style="width:105px;font-size:5px">Lorem ipsum dolor sit amet, consectetuer adipiscing elit, sed diam nonummy nibh euismod tincidunt ut laoreet</div></div>
  <div style="left:417px;top:220px"><div class="h" style="font-size:8px">Lorem ipsum</div><div class="p" style="width:105px;font-size:5px">Lorem ipsum dolor sit amet, consectetuer adipiscing elit, sed diam nonummy nibh euismod tincidunt ut laoreet</div></div>
  <div class="foot"><span class="mark">VANTORA</span><i class="rule"></i><b class="pg"></b></div>
</section>

<!-- 8 Market -->
<section class="slide c2 r3">
  <div class="orange sq" style="left:0;top:0"></div>
  <div style="left:30px;top:32px;font-size:17px;font-weight:700;line-height:1.2">Market<br>Opportunities.</div>
  <div class="dark" style="left:0;top:92px;width:187px;height:152px"></div>
  <div style="left:24px;top:102px;width:150px;color:#fff;font-size:8.2px;line-height:1.2">Lorem ipsum dolor sit amet, consectetuer adipiscing elit, sed diam nonummy nibh euismod tincidunt ut laoreet dolore magna aliquam erat volutpat. Ut wisi enim ad minim veniam, quis nostrud exerci tation ullamcorper suscipit lobortis nisl ut aliquip ex ea commodo consequat. Duis autem vel eum iriure dolor in hendrerit i</div>
  <div style="left:224px;top:38px;font-size:9.5px;font-weight:600">CONSECTETUER ADIPISCING</div>
  <svg style="left:212px;top:60px" width="296" height="152" font-size="9">
    <g stroke="#bbb" stroke-width=".6"><path d="M30 5H293M30 25H293M30 45H293M30 65H293M30 85H293M30 105H293M30 125H293"/><path d="M30 5V125M293 5V125"/></g>
    <g fill="var(--ink)" text-anchor="end"><text x="24" y="9">60</text><text x="24" y="29">50</text><text x="24" y="49">40</text><text x="24" y="69">30</text><text x="24" y="89">20</text><text x="24" y="109">10</text><text x="24" y="129">0</text></g>
    <rect x="49" y="15" width="30" height="110" fill="var(--ink)"/>
    <rect x="107" y="61" width="30" height="64" fill="var(--orange)"/>
    <rect x="164" y="31" width="30" height="94" fill="var(--ink)"/>
    <rect x="222" y="69" width="30" height="56" fill="var(--orange)"/>
    <g text-anchor="middle" fill="var(--ink)"><text x="64" y="142">JAN</text><text x="122" y="142">FEB</text><text x="179" y="142">MAR</text><text x="237" y="142">APR</text></g>
  </svg>
  <svg style="left:209px;top:229px" width="170" height="10"><circle cx="6" cy="5" r="4" fill="var(--orange)"/><circle cx="164" cy="5" r="4" fill="var(--ink)"/></svg>
  <div style="left:224px;top:226px"><div class="h" style="font-size:9px;font-weight:500">Lorem ipsum</div><div class="p" style="width:130px;font-size:5.2px">Lorem ipsum dolor sit amet, consectetuer adipiscing elit, sed diam nonummy nibh euismod tincidunt ut laoreet</div></div>
  <div style="left:381px;top:226px"><div class="h" style="font-size:9px;font-weight:500">Lorem ipsum</div><div class="p" style="width:130px;font-size:5.2px">Lorem ipsum dolor sit amet, consectetuer adipiscing elit, sed diam nonummy nibh euismod tincidunt ut laoreet</div></div>
  <div class="foot"><span class="mark">VANTORA</span><i class="rule"></i><b class="pg"></b></div>
</section>

<!-- 9 Numbered -->
<section class="slide c3 r3">
  <div class="title" style="left:54px;top:27px">Text Added Here</div>
  <div class="photo" role="img" aria-label="Team joining hands over a meeting table" style="left:49px;top:62px;width:160px;height:186px"></div>
  <svg style="left:233px;top:80px" width="30" height="148" font-size="12" font-weight="700" text-anchor="middle">
    <circle cx="14" cy="14" r="14" fill="var(--ink)"/><text x="14" y="18" fill="#fff">1</text>
    <circle cx="14" cy="72" r="14" fill="var(--ink)"/><text x="14" y="76" fill="#fff">2</text>
    <circle cx="14" cy="132" r="14" fill="var(--ink)"/><text x="14" y="136" fill="#fff">3</text>
  </svg>
  <div class="p" style="left:269px;top:82px;width:230px">Lorem ipsum dolor sit amet, consectetuer adipiscing elit, sed diam nonummy nibh euismod tincidunt ut laoreet dolore magna aliquam erat volutpat. Ut wisi enim ad minim veniam, quis nostrud exerci tation</div>
  <div class="p" style="left:269px;top:135px;width:230px">ullamcorper suscipit lobortis nisl ut aliquip ex ea commodo consequat. Duis autem vel eum iriure dolor in hendrerit in<br><br>molestie consequat, vel illum dolore eu feugiat nulla facilisis at vero eros et accumsan et iusto odio dignissim qui blandit nulla facilisi.</div>
  <div class="p" style="left:269px;top:200px;width:230px">Lorem ipsum dolor sit amet, consectetuer adipiscing elit, sed diam nonummy nibh euismod tincidunt ut laoreet dolore magna aliquam erat volutpat. Ut wisi enim ad minim veniam, quis nostrud exerci tation</div>
  <div class="foot"><span class="mark">VANTORA</span><i class="rule"></i><b class="pg"></b></div>
</section>

<!-- 10 Cycle -->
<section class="slide c1 r4">
  <div class="dark sq" style="left:0;top:0"></div>
  <div class="title" style="left:27px;top:35px">Subtitle Text</div>
  <div class="p" style="left:27px;top:68px;width:150px;font-size:7.3px">Lorem ipsum dolor sit amet, consectetuer adipiscing elit, sed diam nonummy nibh .<br><br>Ut wisi enim ad minim veniam, quis nostrud exerci tation ullamcorper suscipit lobortis. Ut wisi enim ad minim veniam, quis nostrud exerci tation ullamcorper suscipit lobortis. Ut wisi enim ad minim veniam, quis</div>
  <div class="orange" style="left:0;top:174px;width:174px;height:82px"></div>
  <svg style="left:28px;top:184px" width="10" height="50"><circle cx="5" cy="5" r="3.5" fill="#fff"/><circle cx="5" cy="42" r="3.5" fill="#fff"/></svg>
  <div style="left:44px;top:181px;color:#fff"><div class="h" style="font-size:8px">Lorem ipsum</div><div class="p w" style="width:110px;font-size:4.6px">Lorem ipsum dolor sit amet, consectetuer adipiscing elit, sed diam nonummy nibh euismod</div></div>
  <div style="left:44px;top:218px;color:#fff"><div class="h" style="font-size:8px">Lorem ipsum</div><div class="p w" style="width:110px;font-size:4.6px">Lorem ipsum dolor sit amet, consectetuer adipiscing elit, sed diam nonummy nibh euismod</div></div>
  <svg style="left:0;top:0" width="543" height="306" font-size="6">
    <path d="M250 120 A95 95 0 1 1 300 238" fill="none" stroke="var(--ink)" stroke-width="4"/>
    <path d="M241 125l9 20 9-20z" fill="var(--ink)"/>
    <path d="M252 180 Q300 260 380 240" fill="none" stroke="var(--ink)" stroke-width="4"/>
    <circle cx="252" cy="180" r="5" fill="var(--ink)"/>
    <g stroke="var(--orange)" fill="#fff">
      <circle cx="406" cy="94" r="28" stroke-width="7"/>
      <circle cx="428" cy="177" r="23" stroke-width="6"/>
      <circle cx="273" cy="213" r="14" stroke-width="4"/>
      <circle cx="384" cy="232" r="14" stroke-width="4"/>
    </g>
    <circle cx="406" cy="94" r="16" fill="var(--orange)"/><circle cx="404" cy="92" r="5" fill="none" stroke="#fff" stroke-width="2"/><path d="M408 96l5 5" stroke="#fff" stroke-width="2"/>
    <circle cx="428" cy="177" r="12" fill="var(--orange)"/><circle cx="428" cy="175" r="4" fill="#fff"/>
    <circle cx="273" cy="213" r="7" fill="var(--orange)"/><circle cx="384" cy="232" r="7" fill="var(--orange)"/>
    <g fill="var(--ink)"><rect x="298" y="114" width="3" height="10"/><rect x="303" y="108" width="3" height="16"/><rect x="308" y="118" width="3" height="6"/><rect x="313" y="112" width="3" height="12" fill="var(--orange)"/></g>
    <text x="281" y="135" font-weight="700" font-size="8" fill="var(--ink)">MAIN TITLE</text>
    <g fill="var(--grey)" font-size="3.8"><text x="281" y="142">Lorem ipsum dolor sit amet,</text><text x="281" y="147">consectetuer adipiscing elit,</text><text x="281" y="152">sed diam nonummy nibh</text></g>
    <g fill="var(--orange)" font-style="italic" font-size="5.5"><text x="454" y="70">85%</text><text x="372" y="151">80%</text><text x="315" y="209">50%</text><text x="424" y="247">75%</text></g>
    <g stroke="var(--orange)" stroke-width=".8" fill="none"><path d="M434 78l18-9M388 150h-8M287 208h26M398 232l24 12"/></g>
    <g font-weight="700" fill="var(--ink)" font-size="6.5"><text x="463" y="84">Your Title</text><text x="475" y="162">Your Title</text><text x="205" y="211">Your Title</text><text x="453" y="229">Your Title</text></g>
    <g fill="var(--grey)" font-size="3.6"><text x="452" y="90">Lorem ipsum dolor sit amet,</text><text x="452" y="95">consectetuer adipiscing elit,</text><text x="452" y="100">sed diam nonummy nibh</text>
      <text x="463" y="168">Lorem ipsum dolor sit amet,</text><text x="463" y="173">consectetuer adipiscing elit,</text>
      <text x="193" y="217">Lorem ipsum dolor sit amet,</text><text x="193" y="222">consectetuer adipiscing elit,</text>
      <text x="441" y="235">Lorem ipsum dolor sit amet,</text><text x="441" y="240">consectetuer adipiscing elit,</text></g>
  </svg>
  <div class="foot"><span class="mark">VANTORA</span><i class="rule"></i><b class="pg"></b></div>
</section>

<!-- 11 Steps with photo -->
<section class="slide c2 r4">
  <div class="orange sq" style="left:0;top:0"></div>
  <div class="title" style="left:32px;top:30px;font-size:18px">Subtitle Text</div>
  <div class="photo" role="img" aria-label="Business team in a meeting room" style="left:31px;top:67px;width:474px;height:140px"></div>
  <div class="orange" style="left:45px;top:199px;width:36px;height:30px;color:#fff;font-weight:700;font-size:15px;text-align:center;line-height:30px">01</div>
  <div class="orange" style="left:210px;top:199px;width:36px;height:30px;color:#fff;font-weight:700;font-size:15px;text-align:center;line-height:30px">02</div>
  <div class="orange" style="left:373px;top:199px;width:36px;height:30px;color:#fff;font-weight:700;font-size:15px;text-align:center;line-height:30px">03</div>
  <div class="p" style="left:86px;top:214px;width:115px;font-size:5.6px">Lorem ipsum Dolor sit<br>amet Consectetur adipiscing<br><br>sed do eiusmod Tempor<br>incididunt ut labore et dolore</div>
  <div class="p" style="left:251px;top:214px;width:115px;font-size:5.6px">Lorem ipsum Dolor sit<br>amet Consectetur adipiscing<br><br>sed do eiusmod Tempor<br>incididunt ut labore et dolore</div>
  <div class="p" style="left:415px;top:214px;width:115px;font-size:5.6px">Lorem ipsum Dolor sit<br>amet Consectetur adipiscing<br><br>sed do eiusmod Tempor<br>incididunt ut labore et dolore</div>
  <div class="foot"><span class="mark">VANTORA</span><i class="rule"></i><b class="pg"></b></div>
</section>

<!-- 12 Timemap -->
<section class="slide c3 r4">
  <div class="title" style="left:16px;top:10px;font-size:16px">Our Timemap</div>
  <svg style="left:0;top:0" width="543" height="260" font-size="7.5">
    <path d="M103 56V208" stroke="#aaa" stroke-width="1"/><circle cx="103" cy="56" r="2" fill="#aaa"/>
    <g font-weight="700" font-size="10" fill="var(--ink)"><text x="69" y="94">2019</text><text x="69" y="134">2020</text><text x="69" y="177">2021</text></g>
    <g fill="var(--ink)"><circle cx="57" cy="90" r="4.5"/><path d="M57 122v12M52 130q5 6 10 0M54 124h6" stroke="var(--ink)" stroke-width="1.5" fill="none"/><circle cx="57" cy="175" r="5"/></g>
    <g fill="#fff" text-anchor="middle">
      <rect x="103" y="74" width="54" height="30" fill="var(--orange)"/><text x="130" y="92">20%</text>
      <rect x="157" y="74" width="75" height="30" fill="var(--ink)"/><text x="194" y="92">40%</text>
      <rect x="232" y="74" width="50" height="30" fill="var(--orange)"/><text x="257" y="92">10%</text>
      <rect x="282" y="74" width="186" height="30" fill="var(--ink)"/><text x="375" y="92">90%</text>
      <rect x="103" y="115" width="129" height="30" fill="var(--ink)"/><text x="167" y="133">50%</text>
      <rect x="232" y="115" width="90" height="30" fill="var(--orange)"/><text x="277" y="133">30%</text>
      <rect x="322" y="115" width="76" height="30" fill="var(--ink)"/><text x="360" y="133">20%</text>
      <rect x="398" y="115" width="70" height="30" fill="var(--orange)"/><text x="433" y="133">20%</text>
      <rect x="103" y="158" width="74" height="30" fill="var(--ink)"/><text x="140" y="176">30%</text>
      <rect x="177" y="158" width="110" height="30" fill="var(--orange)"/><text x="232" y="176">60%</text>
      <rect x="287" y="158" width="35" height="30" fill="var(--ink)"/><text x="304" y="176">10%</text>
      <rect x="322" y="158" width="146" height="30" fill="var(--orange)"/><text x="395" y="176">70%</text>
    </g>
    <path d="M103 202H468" stroke="#bbb" stroke-width=".8"/>
    <g fill="var(--orange)"><circle cx="103" cy="202" r="2"/><circle cx="140" cy="202" r="2"/><circle cx="176" cy="202" r="2"/><circle cx="213" cy="202" r="2"/><circle cx="249" cy="202" r="2"/><circle cx="286" cy="202" r="2"/><circle cx="322" cy="202" r="2"/><circle cx="359" cy="202" r="2"/><circle cx="395" cy="202" r="2"/><circle cx="432" cy="202" r="2"/><circle cx="468" cy="202" r="2"/></g>
    <g fill="var(--ink)" text-anchor="middle"><text x="103" y="218">0%</text><text x="140" y="218">10%</text><text x="176" y="218">20%</text><text x="213" y="218">30%</text><text x="249" y="218">40%</text><text x="286" y="218">50%</text><text x="322" y="218">60%</text><text x="359" y="218">70%</text><text x="395" y="218">80%</text><text x="432" y="218">90%</text><text x="468" y="218">100%</text></g>
  </svg>
  <div style="left:97px;top:234px"><div class="h" style="font-size:7.5px;font-weight:600">Lorem Ipsum</div><div class="p" style="width:90px;font-size:4.6px">Lorem ipsum dolor sit amet, consectetuer adipiscing elit, sed diam nonummy nibh euismod tincid</div></div>
  <div style="left:195px;top:234px"><div class="h" style="font-size:7.5px;font-weight:600">Lorem Ipsum</div><div class="p" style="width:90px;font-size:4.6px">Lorem ipsum dolor sit amet, consectetuer adipiscing elit, sed diam nonummy nibh euismod tincid</div></div>
  <div style="left:299px;top:234px"><div class="h" style="font-size:7.5px;font-weight:600">Lorem Ipsum</div><div class="p" style="width:90px;font-size:4.6px">Lorem ipsum dolor sit amet, consectetuer adipiscing elit, sed diam nonummy nibh euismod tincid</div></div>
  <div style="left:404px;top:234px"><div class="h" style="font-size:7.5px;font-weight:600">Lorem Ipsum</div><div class="p" style="width:90px;font-size:4.6px">Lorem ipsum dolor sit amet, consectetuer adipiscing elit, sed diam nonummy nibh euismod tincid</div></div>
  <div class="foot"><span class="mark">VANTORA</span><i class="rule"></i><b class="pg"></b></div>
</section>

<!-- 13 Two columns -->
<section class="slide c1 r5">
  <div class="title" style="left:17px;top:14px">Text Added Here</div>
  <div class="uline" style="left:17px;top:42px"></div>
  <div style="left:61px;top:58px;width:198px"><div class="h" style="font-size:9.5px;font-weight:600">1. Text Added Here</div><div class="p" style="text-align:justify;margin-top:2px">Lorem ipsum dolor sit amet, cons ectetuer adipiscing elit, sed diam nonummy nibh euismod tincidunt ut laoreet dolore magna aliquam erat volutpat. Ut wisi enim ad minim veniam, quis nostrud exerci tation ullamcorper suscipit lobortis nisl ut aliquip ex ea commodo consequat.<br><br>Lorem ipsum dolor sit amet, consectetuer adipiscing elit, sed diam nonummy nibh euismod tincidunt ut laoreet dolore magna aliquam erat volutpat. Ut wisi enim ad minim veniam, quis nostrud exerci tation ullamcorper suscipit lobortis nisl ut aliquip ex ea commodo consequat.</div></div>
  <div style="left:286px;top:58px;width:198px"><div class="h" style="font-size:9.5px;font-weight:600">2. Text Added Here</div><div class="p" style="text-align:justify;margin-top:2px">Lorem ipsum dolor sit amet, cons ectetuer adipiscing elit, sed diam nonummy nibh euismod tincidunt ut laoreet dolore magna aliquam erat volutpat. Ut wisi enim ad minim veniam, quis nostrud exerci tation ullamcorper suscipit lobortis nisl ut aliquip ex ea commodo consequat.<br><br>Lorem ipsum dolor sit amet, consectetuer adipiscing elit, sed diam nonummy nibh euismod tincidunt ut laoreet dolore magna aliquam erat volutpat. Ut wisi enim ad minim veniam, quis nostrud exerci tation ullamcorper suscipit lobortis nisl ut aliquip ex ea commodo consequat.</div></div>
  <div class="orange" style="left:73px;top:176px;width:22px;height:22px;color:#fff;font-weight:700;font-size:11px;text-align:center;line-height:22px;outline:2px solid #fff;outline-offset:-4px">1.</div>
  <div class="orange" style="left:73px;top:224px;width:22px;height:22px;color:#fff;font-weight:700;font-size:11px;text-align:center;line-height:22px;outline:2px solid #fff;outline-offset:-4px">2.</div>
  <div class="orange" style="left:304px;top:174px;width:22px;height:22px;color:#fff;font-weight:700;font-size:11px;text-align:center;line-height:22px;outline:2px solid #fff;outline-offset:-4px">1.</div>
  <div class="orange" style="left:304px;top:222px;width:22px;height:22px;color:#fff;font-weight:700;font-size:11px;text-align:center;line-height:22px;outline:2px solid #fff;outline-offset:-4px">2.</div>
  <div style="left:103px;top:175px"><div class="h" style="font-size:9px;font-weight:600">Lorem ipsum</div><div class="p" style="width:140px;font-size:5.5px">Lorem ipsum dolor sit amet, consectetuer adipiscing elit, sed diam nonummy nibh</div></div>
  <div style="left:103px;top:223px"><div class="h" style="font-size:9px;font-weight:600">Lorem ipsum</div><div class="p" style="width:140px;font-size:5.5px">Lorem ipsum dolor sit amet, consectetuer adipiscing elit, sed diam nonummy nibh</div></div>
  <div style="left:335px;top:173px"><div class="h" style="font-size:9px;font-weight:600">Lorem ipsum</div><div class="p" style="width:140px;font-size:5.5px">Lorem ipsum dolor sit amet, consectetuer adipiscing elit, sed diam nonummy nibh</div></div>
  <div style="left:335px;top:221px"><div class="h" style="font-size:9px;font-weight:600">Lorem ipsum</div><div class="p" style="width:140px;font-size:5.5px">Lorem ipsum dolor sit amet, consectetuer adipiscing elit, sed diam nonummy nibh</div></div>
  <div class="foot"><span class="mark">VANTORA</span><i class="rule"></i><b class="pg"></b></div>
</section>

<!-- 14 Icon grid -->
<section class="slide c2 r5">
  <div class="title" style="left:17px;top:14px">Text Added Here</div>
  <div class="uline" style="left:17px;top:42px"></div>
  <svg style="left:0;top:0" width="543" height="270" font-size="8.5" text-anchor="middle">
    <g stroke="#fff" stroke-width="1.6" fill="none">
      <rect x="94" y="60" width="42" height="42" fill="var(--ink)" stroke="none"/><circle cx="109" cy="77" r="4"/><circle cx="121" cy="77" r="4"/><path d="M102 92c0-6 14-6 14 0M114 92c0-6 14-6 14 0"/>
      <rect x="250" y="60" width="42" height="42" fill="var(--orange)" stroke="none"/><circle cx="265" cy="77" r="6"/><circle cx="277" cy="86" r="5"/>
      <rect x="406" y="60" width="42" height="42" fill="var(--ink)" stroke="none"/><path d="M415 93h24M418 93v-6h4v6M425 93v-10h4v10M432 93v-14h4v14M416 80l8-6 6 3 8-8"/>
      <rect x="94" y="170" width="42" height="42" fill="var(--orange)" stroke="none"/><path d="M104 180v22h22M106 184l8 12 10-4"/>
      <rect x="250" y="170" width="42" height="42" fill="var(--ink)" stroke="none"/><path d="M264 184h14l4 18h-22zM266 184l3-5h4l3 5"/><text x="271" y="199" fill="#fff" stroke="none" font-size="9" font-weight="700">$</text>
      <rect x="406" y="170" width="42" height="42" fill="var(--orange)" stroke="none"/><circle cx="427" cy="188" r="8"/><path d="M421 195l-3 10 5-2 4 4M433 195l3 10-5-2-4 4"/>
    </g>
    <g font-weight="600" fill="var(--ink)"><text x="115" y="120">Lorem ipsum</text><text x="271" y="120">Lorem ipsum</text><text x="427" y="120">Lorem ipsum</text><text x="115" y="229">Lorem ipsum</text><text x="271" y="229">Lorem ipsum</text><text x="427" y="229">Lorem ipsum</text></g>
    <g fill="var(--grey)" font-size="5">
      <text x="115" y="128">Lorem ipsum dolor sit amet,</text><text x="115" y="134">consectetuer adipiscing elit, sed</text><text x="115" y="140">diam nonummy nibh euismod</text><text x="115" y="146">tincidunt ut laoreet</text>
      <text x="271" y="128">Lorem ipsum dolor sit amet,</text><text x="271" y="134">consectetuer adipiscing elit, sed</text><text x="271" y="140">diam nonummy nibh euismod</text><text x="271" y="146">tincidunt ut laoreet</text>
      <text x="427" y="128">Lorem ipsum dolor sit amet,</text><text x="427" y="134">consectetuer adipiscing elit, sed</text><text x="427" y="140">diam nonummy nibh euismod</text><text x="427" y="146">tincidunt ut laoreet</text>
      <text x="115" y="237">Lorem ipsum dolor sit amet,</text><text x="115" y="243">consectetuer adipiscing elit, sed</text><text x="115" y="249">diam nonummy nibh euismod</text><text x="115" y="255">tincidunt ut laoreet</text>
      <text x="271" y="237">Lorem ipsum dolor sit amet,</text><text x="271" y="243">consectetuer adipiscing elit, sed</text><text x="271" y="249">diam nonummy nibh euismod</text><text x="271" y="255">tincidunt ut laoreet</text>
      <text x="427" y="237">Lorem ipsum dolor sit amet,</text><text x="427" y="243">consectetuer adipiscing elit, sed</text><text x="427" y="249">diam nonummy nibh euismod</text><text x="427" y="255">tincidunt ut laoreet</text>
    </g>
  </svg>
  <div class="foot"><span class="mark">VANTORA</span><i class="rule"></i><b class="pg"></b></div>
</section>

<!-- 15 Process -->
<section class="slide c3 r5">
  <div class="title" style="left:17px;top:14px">Text Added Here</div>
  <div class="uline" style="left:17px;top:42px"></div>
  <svg style="left:0;top:0" width="543" height="270" text-anchor="middle">
    <rect x="42" y="140" width="455" height="8" fill="var(--ink)"/>
    <rect x="225" y="140" width="75" height="8" fill="var(--orange)"/>
    <rect x="416" y="140" width="81" height="8" fill="var(--orange)"/>
    <path d="M497 136l9 8-9 8z" fill="var(--orange)"/>
    <g fill="none" stroke-width="8">
      <circle cx="130" cy="116" r="27" stroke="var(--ink)"/>
      <circle cx="225" cy="116" r="27" stroke="var(--orange)"/>
      <circle cx="321" cy="116" r="27" stroke="var(--ink)"/>
      <circle cx="416" cy="116" r="27" stroke="var(--orange)"/>
    </g>
    <circle cx="130" cy="116" r="9" fill="none" stroke="var(--orange)" stroke-width="2"/><path d="M130 110v6h4" stroke="var(--orange)" stroke-width="1.5" fill="none"/>
    <circle cx="225" cy="118" r="9" fill="var(--ink)"/><text x="225" y="122" fill="#fff" font-size="9" font-weight="700">$</text>
    <g fill="var(--orange)"><ellipse cx="321" cy="110" rx="9" ry="3"/><rect x="312" y="112" width="18" height="3"/><rect x="312" y="117" width="18" height="3"/><rect x="312" y="122" width="18" height="3"/></g>
    <circle cx="418" cy="113" r="6" fill="none" stroke="var(--ink)" stroke-width="2"/><path d="M414 118l-5 6" stroke="var(--ink)" stroke-width="2"/>
    <g fill="#fff" font-size="6" font-weight="700"><text x="144" y="146">Step 01</text><text x="248" y="146">Step 02</text><text x="336" y="146">Step 03</text><text x="452" y="146">Step 04</text></g>
    <g stroke="#999" stroke-width="1"><path d="M130 150v18M225 150v18M321 150v18M416 150v18"/></g>
    <g fill="#999"><circle cx="130" cy="168" r="1.8"/><circle cx="225" cy="168" r="1.8"/><circle cx="321" cy="168" r="1.8"/><circle cx="416" cy="168" r="1.8"/></g>
    <g font-size="9" font-weight="600" fill="var(--ink)"><text x="130" y="188">Lorem Ipsum</text><text x="225" y="188">Lorem Ipsum</text><text x="321" y="188">Lorem Ipsum</text><text x="416" y="188">Lorem Ipsum</text></g>
    <g font-size="4.6" fill="var(--grey)">
      <text x="130" y="196">Lorem ipsum dolor sit</text><text x="130" y="201">amet, consectetuer</text><text x="130" y="206">adipiscing elit, sed diam</text><text x="130" y="211">nonummy nibh euismod</text><text x="130" y="216">tincidunt ut laoreet</text><text x="130" y="221">dolore magna aliquam</text>
      <text x="225" y="196">Lorem ipsum dolor sit</text><text x="225" y="201">amet, consectetuer</text><text x="225" y="206">adipiscing elit, sed diam</text><text x="225" y="211">nonummy nibh euismod</text><text x="225" y="216">tincidunt ut laoreet</text><text x="225" y="221">dolore magna aliquam</text>
      <text x="321" y="196">Lorem ipsum dolor sit</text><text x="321" y="201">amet, consectetuer</text><text x="321" y="206">adipiscing elit, sed diam</text><text x="321" y="211">nonummy nibh euismod</text><text x="321" y="216">tincidunt ut laoreet</text><text x="321" y="221">dolore magna aliquam</text>
      <text x="416" y="196">Lorem ipsum dolor sit</text><text x="416" y="201">amet, consectetuer</text><text x="416" y="206">adipiscing elit, sed diam</text><text x="416" y="211">nonummy nibh euismod</text><text x="416" y="216">tincidunt ut laoreet</text><text x="416" y="221">dolore magna aliquam</text>
    </g>
  </svg>
  <div class="foot"><span class="mark">VANTORA</span><i class="rule"></i><b class="pg"></b></div>
</section>

<!-- 16 Creative -->
<section class="slide c1 r6">
  <div class="orange" style="left:0;top:0;width:25px;height:28px"></div>
  <div style="left:40px;top:44px;font-size:17px;font-weight:700;line-height:1.35">Creative Text<br>Heading Added<br>Here</div>
  <div class="photo warm" role="img" aria-label="Colleagues gathered around a laptop in a meeting" style="left:211px;top:41px;width:332px;height:127px"></div>
  <div style="left:44px;top:148px;width:15px;height:15px;border:1.5px solid var(--ink);font-weight:700;font-size:10px;text-align:center;line-height:12px">1.</div>
  <div style="left:44px;top:185px;width:15px;height:15px;border:1.5px solid var(--ink);font-weight:700;font-size:10px;text-align:center;line-height:12px">2.</div>
  <div style="left:44px;top:222px;width:15px;height:15px;border:1.5px solid var(--ink);font-weight:700;font-size:10px;text-align:center;line-height:12px">3.</div>
  <div style="left:67px;top:143px"><div style="font-size:7.5px;color:var(--orange);font-weight:500">Lorem ipsum</div><div class="p" style="width:110px;font-size:4.8px">Lorem ipsum dolor sit amet, consectetuer adipiscing elit, sed diam nonummy nibh</div></div>
  <div style="left:67px;top:180px"><div style="font-size:7.5px;color:var(--orange);font-weight:500">Lorem ipsum</div><div class="p" style="width:110px;font-size:4.8px">Lorem ipsum dolor sit amet, consectetuer adipiscing elit, sed diam nonummy nibh</div></div>
  <div style="left:67px;top:217px"><div style="font-size:7.5px;color:var(--orange);font-weight:500">Lorem ipsum</div><div class="p" style="width:110px;font-size:4.8px">Lorem ipsum dolor sit amet, consectetuer adipiscing elit, sed diam nonummy nibh</div></div>
  <div class="p" style="left:211px;top:173px;width:318px;font-size:7.2px">Lorem ipsum dolor sit amet, consectetuer adipiscing elit, sed diam nonummy nibh euismod tincidunt erat volutpat.<br><br>Ut wisi enim ad minim veniam, quis nostrud exerci tation ullamcorper suscipit lobortis nisl ut aliquip ex ea commodo consequat. Ut wisi enim ad minim veniam, quis nostrud exerci tation ullamcorper suscipit lobortis nisl ut aliquip ex ea commodo consequat.</div>
  <div class="foot"><span class="mark">VANTORA</span><i class="rule"></i><b class="pg"></b></div>
</section>

<!-- 17 Team -->
<section class="slide c2 r6">
  <div class="title" style="left:26px;top:22px">Our Team Members</div>
  <div class="uline" style="left:26px;top:47px"></div>
  <div class="p" style="left:26px;top:58px;width:500px;font-size:6.3px">Lorem ipsum dolor sit amet, consectetuer adipiscing elit, sed diam nonummy nibh euismod tincidunt ut laoreet dolore magna aliquam erat volutpat. Ut wisi enim ad minim veniam, quis nostrud exerci tation ullamcorper suscipit lobortis nisl ut aliquip ex ea commodo consequat. Duis autem vel eum iriure dolor in hendrerit in vulputate velit esse molestie consequat, vel illum dolore eu feugiat nulla facilisis at vero eros et accumsan et iusto odio dignissim qui blandit praesent luptatum zzril delenit augue duis dolore te feugait nulla facilisi.<br><br>Lorem ipsum dolor sit amet, cons ectetuer adipiscing elit, sed diam nonummy nibh euismod tincidunt ut laoreet dolore magna aliquam erat volutpat. Ut wisi enim ad minim veniam, quis nostrud exerci tation ullamcorper suscipit lobortis nisl ut aliquip ex</div>
  <div class="dark" style="left:0;top:157px;width:543px;height:98px"></div>
  <svg style="left:0;top:128px" width="543" height="130" text-anchor="middle">
    <g fill="#e4e4e4" stroke="var(--orange)" stroke-width="2.5">
      <circle cx="74" cy="27" r="23"/><circle cx="205" cy="27" r="23"/><circle cx="332" cy="27" r="23"/><circle cx="463" cy="27" r="23"/>
    </g>
    <g fill="#fff" font-weight="700" font-size="8.5"><text x="74" y="66">ALEX RIVERA</text><text x="205" y="66">NORA VANCE</text><text x="332" y="66">ALEX RIVERA</text><text x="463" y="66">NORA VANCE</text></g>
    <g fill="#fff" font-size="3.8">
      <text x="74" y="74">Ipsum dolor sit amet, cons</text><text x="74" y="79">ectetuer adipiscing elit, sed diam</text><text x="74" y="84">nonummy nibh euismod</text><text x="74" y="89">tincidunt ut laoreet dolore</text><text x="74" y="94">magna aliquam erat volutpat.</text>
      <text x="205" y="74">Ipsum dolor sit amet, cons</text><text x="205" y="79">ectetuer adipiscing elit, sed diam</text><text x="205" y="84">nonummy nibh euismod</text><text x="205" y="89">tincidunt ut laoreet dolore</text><text x="205" y="94">magna aliquam erat volutpat.</text>
      <text x="332" y="74">Ipsum dolor sit amet, cons</text><text x="332" y="79">ectetuer adipiscing elit, sed diam</text><text x="332" y="84">nonummy nibh euismod</text><text x="332" y="89">tincidunt ut laoreet dolore</text><text x="332" y="94">magna aliquam erat volutpat.</text>
      <text x="463" y="74">Ipsum dolor sit amet, cons</text><text x="463" y="79">ectetuer adipiscing elit, sed diam</text><text x="463" y="84">nonummy nibh euismod</text><text x="463" y="89">tincidunt ut laoreet dolore</text><text x="463" y="94">magna aliquam erat volutpat.</text>
    </g>
  </svg>
  <div class="foot"><span class="mark">VANTORA</span><i class="rule"></i><b class="pg"></b></div>
</section>

<!-- 18 Closing -->
<section class="slide c3 r6">
  <div style="left:0;top:36px;width:543px;text-align:center;font-weight:800;font-size:30px;letter-spacing:1px">VANTORA</div>
  <div style="left:0;top:120px;width:212px;text-align:right;font-size:42px;font-weight:700;line-height:1.15">Thank<br>You</div>
  <div class="photo" role="img" aria-label="Team discussing charts in a modern office" style="left:230px;top:118px;width:197px;height:150px"></div>
  <div class="orange" style="left:432px;top:118px;width:28px;height:150px"></div>
  <div class="dark" style="left:12px;top:270px;width:22px;height:22px"></div>
</section>

</div>
</body>
</html>
```